Tallowreed Advisory Partners Business Card Design

We have the logo we just need someone to design a modern business card design.

Name: Desmond Munkalt
Phone: 3055550148
Mobile: 9175550193
Web:www.tallowreedadvisory.example
email: dmunkalt@tallowreedadvisory.example
Company: Tallowreed Advisory Partners
Title: CEO

Address: 718 Quillmore Ave, Miami, Florida 33190

Target Market(s)

companies over 100 employees

Industry/Entity Type

Business

```html
<!DOCTYPE html>
<html lang="en">
<head>
<meta charset="utf-8">
<title>Tallowreed Advisory Partners – Business Card</title>
<link rel="stylesheet" href="https://fonts.googleapis.com/css2?family=Open+Sans:wght@400;600;700&display=swap">
<style>
  :root {
    --brand-blue: #0b5fef;
    --card-white: #ffffff;
    --ink: #1c1c1c;
    --ink-soft: #3a3a3a;
    --backdrop: #e9e9ec;
    --shadow: rgba(0, 0, 0, 0.14);
  }
  * { box-sizing: border-box; margin: 0; padding: 0; }
  html, body {
    width: 1200px;
    height: 873px;
    overflow: hidden;
    background: var(--backdrop);
    font-family: "Open Sans", Arial, sans-serif;
  }
  .canvas {
    position: relative;
    width: 1200px;
    height: 873px;
    display: flex;
    align-items: center;
    justify-content: center;
    gap: 60px;
  }
  .card {
    position: relative;
    width: 520px;
    height: 297px;
    background: var(--card-white);
    box-shadow: 0 6px 22px var(--shadow);
    overflow: hidden;
  }

  /* Front: contact side */
  .contact-block {
    position: absolute;
    left: 34px;
    top: 30px;
    color: var(--ink);
  }
  .person-name {
    font-size: 24px;
    font-weight: 400;
    letter-spacing: 0.2px;
  }
  .person-title {
    font-size: 12px;
    color: var(--ink-soft);
    margin-top: 2px;
  }
  .address {
    margin-top: 22px;
    font-size: 12.5px;
    line-height: 1.35;
    font-style: normal;
    color: var(--ink);
  }
  .front-mark {
    position: absolute;
    right: 34px;
    bottom: 62px;
    display: flex;
    align-items: center;
    gap: 8px;
  }
  .front-mark .mark-dot {
    width: 26px;
    height: 26px;
    border-radius: 50%;
    background: var(--brand-blue);
  }
  .front-mark .mark-name {
    font-size: 17px;
    font-weight: 700;
    color: var(--ink);
    letter-spacing: 1px;
  }
  .web-band {
    position: absolute;
    left: 0;
    right: 0;
    bottom: 0;
    height: 28px;
    background: var(--brand-blue);
    display: flex;
    align-items: center;
    justify-content: space-between;
    padding: 0 22px;
    color: var(--card-white);
    font-size: 11.5px;
  }

  /* Back: brand side */
  .brand-band {
    position: absolute;
    left: 0;
    right: 0;
    top: 62px;
    height: 150px;
    background: var(--brand-blue);
    display: flex;
    flex-direction: column;
    align-items: center;
    justify-content: center;
    gap: 12px;
  }
  .brand-band .mark-dot {
    width: 50px;
    height: 50px;
    border-radius: 50%;
    background: var(--card-white);
  }
  .brand-band .mark-name {
    font-size: 28px;
    font-weight: 700;
    letter-spacing: 2px;
    color: var(--card-white);
  }
</style>
</head>
<body>
  <main class="canvas">
    <section class="card card-front" aria-label="Business card front">
      <div class="contact-block">
        <h1 class="person-name">Desmond Munkalt</h1>
        <p class="person-title">Chief Executive Officer</p>
        <address class="address">
          718 Quillmore Ave.<br>
          Miami, Florida 33190<br>
          Tel: 3055550148<br>
          Cell: 9175550193
        </address>
      </div>
      <div class="front-mark">
        <span class="mark-dot" aria-hidden="true"></span>
        <span class="mark-name">Tallowreed</span>
      </div>
      <div class="web-band">
        <span class="email">dmunkalt@tallowreedadvisory.example</span>
        <span class="website">www.tallowreedadvisory.example</span>
      </div>
    </section>

    <section class="card card-back" aria-label="Business card back">
      <div class="brand-band">
        <span class="mark-dot" aria-hidden="true"></span>
        <span class="mark-name">Tallowreed</span>
      </div>
    </section>
  </main>
</body>
</html>
```